Little Ones Can Soar
Brochure
onescansoar.org
I have a logo that was created by brand (business cards) mark maven and a web site that was designed by pixel sage, I am interested in intergrating those designs into two or tri fold business brochure. Your company has all the records that are needed
Corporate, businesses, retailers, Individuals and people of all walks of life. (prospects of give)
Need a brochure not expensive to print. What would be you suggestion as to the type of brochure needed?

```html
<!DOCTYPE html>
<html lang="en">
<head>
<meta charset="utf-8">
<title>Little Ones Can Soar — Brochure</title>
<link rel="stylesheet" href="https://fonts.googleapis.com/css2?family=Arimo:wght@400;700&family=Lora:ital,wght@0,700;1,700&display=swap">
<style>
:root{
  --green-dark:#1f4a22;
  --green:#3c7a2e;
  --green-light:#8cbf3f;
  --orange:#e0651a;
  --red:#c8281e;
  --yellow:#f2c21b;
  --ink:#222;
  --paper:#fff;
  --canvas:#e9e9e9;
}
*{box-sizing:border-box;margin:0;padding:0}
html,body{width:1200px;height:598px;overflow:hidden;background:var(--canvas)}
body{font-family:'Arimo',Arial,sans-serif;color:var(--ink)}
.brochure{position:relative;width:1200px;height:598px;display:flex}
.panel{position:relative;width:300px;height:598px;background:var(--paper);overflow:hidden;border-right:1px solid #d6d6d6}
.panel:last-child{border-right:none}
.fill{position:absolute}
.brand{display:flex;align-items:center;gap:8px;font-family:'Lora',Georgia,serif;font-weight:700;color:var(--orange)}
.brand .dot{width:16px;height:16px;border-radius:50%;background:var(--green-light);flex:none}
.band{position:absolute;left:0;right:0;background:var(--green-dark);color:#fff;padding:10px 16px}
.band h3{font-size:14px;font-weight:700}
.band p{font-size:11px;margin-top:3px}
.fine{position:absolute;left:0;right:0;font-size:7px;color:#333;text-align:center}
.head{font-family:'Lora',Georgia,serif;font-weight:700;font-size:13px;line-height:1.2;color:var(--ink)}
.head .cap{font-size:22px;color:var(--ink)}
.text{font-size:9.5px;line-height:1.3}
ul.goals{list-style:none;font-size:10px;line-height:1.3}
ul.goals li::before{content:"■ ";color:var(--green);font-size:7px}
.section{position:absolute;left:14px;right:14px}
.lead-bar{position:absolute;top:0;left:0;right:0;height:28px;background:var(--green-dark);color:#fff;font-family:'Lora',Georgia,serif;font-size:15px;padding:5px 16px}
.about{font-family:'Lora',Georgia,serif;font-style:italic;font-weight:700;color:var(--orange);font-size:13px}
.photos{position:absolute;display:flex;gap:4px}
.photos div{flex:1}
</style>
</head>
<body>
<main class="brochure">

  <section class="panel cover-back">
    <div class="brand" style="position:absolute;left:18px;top:26px;font-size:26px;line-height:1.05;width:220px">
      <span class="dot"></span><span>Little Ones<br>Can Soar</span>
    </div>
    <div class="fill" role="img" aria-label="Photo of a smiling child at a desk" style="left:0;top:130px;width:300px;height:340px;background:linear-gradient(160deg,#d9c3a8,#a98a6c 55%,#6d7f5a)"></div>
    <div class="band" style="top:468px;height:78px">
      <h3>Non-Profit Organization 501(c)3</h3>
      <p>Helping students with basic skills</p>
    </div>
    <p class="fine" style="top:572px">1200 Harbor Lane, Suite 4 · Riverside, NJ 08000 · 555-0142 · onescansoar.org</p>
  </section>

  <section class="panel goals-panel">
    <div class="section" style="top:10px">
      <h2 class="head"><span class="cap">O</span>ur goals as an organization are:</h2>
      <ul class="goals" style="margin-top:3px">
        <li>Understand urban school problems</li>
        <li>Adapt to education model for communities to achieve</li>
        <li>Create partnership and strategic alliances to improve the learning process in communities</li>
        <li>Understand kids need gifts of school supplies, backpacks, uniforms, and other essential tools to function in school.</li>
      </ul>
    </div>
    <div class="photos" style="left:150px;right:14px;top:150px;height:62px">
      <div role="img" aria-label="Photo of children reading" style="background:#c7a178"></div>
      <div role="img" aria-label="Photo of a student writing" style="background:#8f6c4e"></div>
    </div>
    <div class="section" style="top:178px;right:160px">
      <h2 class="head"><span class="cap">V</span><em>olunteer</em></h2>
    </div>
    <p class="text section" style="top:220px">Please take this opportunity to get involved, by volunteering your talent and skills in a worthwhile cause. Volunteers are the fiber of our organization. If you are interested in becoming a volunteer and want to learn more about us, just forward us an e-mail.</p>
    <div class="section" style="top:290px">
      <h2 class="head"><span class="cap">I</span><em>nvitation</em></h2>
    </div>
    <p class="text section" style="top:322px">Little Ones Can Soar Inc. hopes that your company is interested in supporting our mission by enhancing the image of your company's community involvement.<br><br>We would like companies to be part of our mission and be given an extended invitation. Corporate sponsorship raises awareness in the community. Bridge the gap in helping local kids by providing the essential tools to succeed and making our schools a better place to learn. Your support will give immediate return on your charitable contribution.</p>
    <div class="fill" role="img" aria-label="Illustration of colored pencils and crayons" style="left:0;bottom:0;width:300px;height:70px;background:linear-gradient(90deg,var(--red),var(--yellow),var(--green-light),#3a7bd5)"></div>
  </section>

  <section class="panel leadership">
    <div class="lead-bar">Leadership Team</div>
    <div class="fill" role="img" aria-label="Portrait photo of the founder" style="left:14px;top:42px;width:70px;height:78px;background:linear-gradient(#bfae9c,#6b5b4d)"></div>
    <p class="text" style="position:absolute;left:14px;top:124px;width:74px;font-size:7px">Dana Whitlow<br>President &amp; CEO</p>
    <p class="text" style="position:absolute;left:94px;right:14px;top:40px">Dana Whitlow is the founder of the organization since its inception, a native of Jacksonville, FL. Dana was a territory manager for 15 years, responsible for selling and maintaining a 4 million $ territory in central New Jersey. Dana worked twenty-two years as an operational auditor for Metro Rail Authority.</p>
    <p class="about section" style="top:160px">About Us at Little Ones Can Soar Inc.</p>
    <p class="text section" style="top:180px">Little Ones Can Soar Inc. mission is to enrich kids learning by providing the essential tools to succeed. The experiences the kids will have while participating in the company's programs will assist them in making their transition from grade level to grade level more smoothly. This resource will allow them to develop their skill sets that will be implemented in advanced grades.</p>
    <div class="photos" style="left:150px;right:14px;top:262px;height:48px">
      <div role="img" aria-label="Photo of students in class" style="background:#b48a62"></div>
      <div role="img" aria-label="Photo of a teacher helping a child" style="background:#7f8f6a"></div>
    </div>
    <p class="text section" style="top:316px">Kids should be taught how to communicate, speak and interact with peers appropriately. They should be provided various materials, games and activities to be introduced to learn in the areas of language, vocabulary, reading, mathematics, science, computers and social behaviors (discipline). Underserved kids need gifts of school supplies, backpacks, uniforms, and other essential tools to function in school.<br>The demographic market has changed in the urban areas. Kids need help. Parents are losing their jobs and cannot provide for their kids basic educational necessities.</p>
    <div class="fill" role="img" aria-label="Illustration of a guitar and music notes" style="left:0;bottom:0;width:300px;height:100px;background:linear-gradient(120deg,var(--yellow),var(--orange) 50%,var(--green))"></div>
  </section>

  <section class="panel cover-front">
    <div class="fill" role="img" aria-label="Photo of joined hands in a circle" style="left:12px;top:12px;width:276px;height:230px;background:radial-gradient(circle at 50% 50%,#e8d6c2,#9a7e64 70%,#4a4038)"></div>
    <p style="position:absolute;right:14px;top:252px;font-size:10px;font-style:italic">Join us in our project</p>
    <div class="band" style="top:300px;height:60px">
      <h3>Non-Profit Organization 501(c)3</h3>
      <p>Helping students with basic skills</p>
      <p style="font-size:7px;margin-top:2px">555-0142 · info@onescansoar.org</p>
    </div>
    <div class="brand" style="position:absolute;right:16px;bottom:20px;font-size:15px;line-height:1.05">
      <span class="dot"></span><span>Little Ones<br>Can Soar</span>
    </div>
  </section>

</main>
</body>
</html>
```